ARC VOLLEY Business Card Project

I'd like to request a business card design for the new company I've launched.
The name of the company is "ARC VOLLEY" an indoor unmanned tennis practice facility.
We would like to see designs that use our brand identity color in the logo I've attached.
We hope to get the design with modern, luxurious and elegant tone and manner.
We hope the logo should not be too big.

Business card must have elements as below:
- Logo (One of the logos I've attached)
- Name (In Korean Text) : 박 서 윤
- Title (In Korean Text) : 대표
- Phone Number : 010-8472-3916
- Email Address : seoyun.park@arcvolley-example.co.kr
- Website : www.arcvolley-example.co.kr
- Instagram : arcvolley
- Address (In Korean text) : 경기도 용인시 수지구 풍덕천로 456 미래타워 5층 501호, 502호

Target Market(s)

Tennis amateurs in 20 to 40s

Industry/Entity Type

Sports, Hobby

Contact Information for Business Card

- Logo (One of the logos I've attached) - Name (In Korean Text) : 박 서 윤 - Title (In Korean Text) : 대표 - Phone Number : 010-8472-3916 - Email Address : seoyun.park@arcvolley-example.co.kr - Website : www.arcvolley-example.co.kr - Instagram : arcvolley - Address (In Korean text) : 경기도 용인시 수지구 풍덕천로 456 미래타워 5층 501호, 502호

Font styles to use
Sans Serif

Requirements
Must have
• Double sided
Nice to have
• Logo with intaglio or relief embossing
Should not have
• Logo should not be too big.

```html
<!DOCTYPE html>
<html lang="ko">
<head>
<meta charset="utf-8">
<title>ARC VOLLEY Business Card</title>
<link href="https://fonts.googleapis.com/css2?family=Noto+Sans+KR:wght@400;500;700&family=Noto+Serif:wght@400;600&display=swap" rel="stylesheet">
<style>
  :root {
    --backdrop: #8e8e8e;
    --card-white: #ffffff;
    --brand-green: #2e5139;
    --ink-dark: #2b2b2b;
    --ink-grey: #666666;
    --rule: #3a3a3a;
  }
  * { margin: 0; padding: 0; box-sizing: border-box; }
  html, body {
    width: 1200px; height: 1200px; overflow: hidden;
    background: var(--backdrop);
  }
  .canvas { position: relative; width: 1200px; height: 1200px; }
  .card {
    position: absolute; left: 281px; width: 642px; height: 366px;
    border-radius: 18px; overflow: hidden;
  }
  .card--front { top: 195px; background: var(--card-white); }
  .card--back { top: 639px; background: var(--brand-green); }

  .person { position: absolute; left: 45px; top: 110px; font-family: "Noto Sans KR", sans-serif; }
  .person__name { font-size: 29px; font-weight: 500; color: var(--brand-green); line-height: 1.1; letter-spacing: 1px; }
  .person__title { font-size: 18px; font-weight: 400; color: var(--ink-grey); margin-top: 4px; }

  .contact { position: absolute; left: 47px; top: 192px; list-style: none; }
  .contact__item { display: flex; align-items: flex-start; gap: 8px; color: var(--ink-dark); }
  .contact__icon { width: 11px; height: 11px; flex: none; fill: var(--brand-green); margin-top: 3px; }
  .contact__item--address { font-family: "Noto Sans KR", sans-serif; font-size: 12px; font-weight: 700; line-height: 16px; margin-bottom: 6px; }
  .contact__item--latin { font-family: "Noto Serif", serif; font-size: 14px; line-height: 19.5px; }
  .contact__item--phone { font-size: 15px; }
  .contact__item--latin .contact__icon { margin-top: 5px; }

  .brand-mark {
    position: absolute; right: 47px; top: 270px;
    font-family: "Noto Serif", serif; font-weight: 600;
    font-size: 25px; letter-spacing: 1px; color: var(--brand-green); line-height: 1;
  }
  .divider { position: absolute; left: 46px; right: 47px; top: 306px; height: 1px; background: var(--rule); }
  .website {
    position: absolute; left: 47px; top: 315px;
    font-family: "Noto Serif", serif; font-size: 13.5px; letter-spacing: 1px; color: var(--brand-green);
  }

  .card--back .brand-mark--center {
    position: absolute; left: 0; right: 0; top: 160px; text-align: center;
    font-family: "Noto Serif", serif; font-weight: 600;
    font-size: 38px; letter-spacing: 2px; color: var(--card-white); line-height: 1;
  }
</style>
</head>
<body>
<main class="canvas">
  <section class="card card--front" aria-label="Business card front">
    <div class="person">
      <p class="person__name">박서윤</p>
      <p class="person__title">대표</p>
    </div>
    <ul class="contact">
      <li class="contact__item contact__item--address">
        <svg class="contact__icon" viewBox="0 0 12 12"><path d="M6 0C3.6 0 2 1.7 2 4c0 3 4 8 4 8s4-5 4-8C10 1.7 8.4 0 6 0zm0 5.6A1.6 1.6 0 1 1 6 2.4a1.6 1.6 0 0 1 0 3.2z"/></svg>
        <span>경기도 용인시 수지구 풍덕천로<br>456 미래타워 5층 501호, 502호</span>
      </li>
      <li class="contact__item contact__item--latin contact__item--phone">
        <svg class="contact__icon" viewBox="0 0 12 12"><path d="M2.4 0.6l2 2-1 1.4c.7 1.6 2 2.9 3.6 3.6l1.4-1 2 2-1.2 1.8C5 10 2 7 1 2.2z"/></svg>
        <span>010-8472-3916</span>
      </li>
      <li class="contact__item contact__item--latin">
        <svg class="contact__icon" viewBox="0 0 12 12"><path d="M0 2h12v1.2L6 7 0 3.2zM0 4.6l6 3.8 6-3.8V10H0z"/></svg>
        <span>seoyun.park@arcvolley-example.co.kr</span>
      </li>
      <li class="contact__item contact__item--latin">
        <svg class="contact__icon" viewBox="0 0 12 12"><circle cx="6" cy="6" r="4.6" fill="none" stroke="var(--brand-green)" stroke-width="1.4"/></svg>
        <span>arcvolley</span>
      </li>
    </ul>
    <p class="brand-mark">ARC VOLLEY</p>
    <div class="divider"></div>
    <p class="website">ARCVOLLEY-EXAMPLE.CO.KR</p>
  </section>

  <section class="card card--back" aria-label="Business card back">
    <p class="brand-mark--center">ARC VOLLEY</p>
  </section>
</main>
</body>
</html>
```